Business card design needed

I have started a new business called Marlow Auto Electrical, although the words Marlow Auto Electrical will be used on signage and documents I actually want to market the business as MAE. The services I offer are Mobile Auto Electrical, Automotive Air Conditioning and Test And Tag. My business will be targetting the Mining Industry, Civil, Rail, Agricultural and Workshop Testing And Tagging. My auto electrical service ranges from fault finding to new vehicle and mine compliance fit outs. I have a very strong focus on quality workmanship. I will upload the logo I have designed and want to use I am happy for the logo colour to change but the design itself must stay the same. I want the design to have a modern, eye catching, energetic feel. As I am a passionate motorsport fan I am happy for this to also influence the design. I am happy for the front of the card to have only the emblem and logo design and the back to have all the info.

Industry/Entity Type

Electrical

Contact Information for Business Card

MAE Marlow Auto Electrical, Glen Tavish, Auto Electrician, Mobile No 0417268354

Requirements
Must have
• On the business card it is mandatory that the following license numbers are shown:

MVRL83742
PXB L731406
ABN 48 913 260 154

```html
<!DOCTYPE html>
<html lang="en">
<head>
<meta charset="utf-8">
<title>Marlow Auto Electrical – Business Card</title>
<link rel="stylesheet" href="https://fonts.googleapis.com/css2?family=Roboto+Condensed:wght@400;700&display=swap">
<style>
  :root {
    --stage: #e7e4df;
    --card: #2a2a2a;
    --card-light: #383838;
    --frame: #5a5a5a;
    --yellow: #f0ec1e;
    --white: #ffffff;
    --ink: #e9e9e9;
    --font: "Roboto Condensed", Arial, sans-serif;
  }
  * { margin: 0; padding: 0; box-sizing: border-box; }
  html, body { width: 1200px; height: 1000px; overflow: hidden; }
  body { background: var(--stage); font-family: var(--font); position: relative; }

  .card {
    position: absolute;
    left: 210px;
    width: 780px;
    height: 442px;
    background: var(--card);
    overflow: hidden;
  }
  .card--front { top: 38px; }
  .card--back  { top: 520px; }

  /* Front */
  .front-shade { position: absolute; inset: 0; }
  .front-brand {
    position: absolute;
    left: 95px;
    top: 120px;
    width: 520px;
    transform: rotate(-20deg);
    transform-origin: center;
    text-align: center;
  }
  .front-brand__name {
    display: block;
    font-weight: 700;
    font-size: 170px;
    line-height: 0.9;
    color: var(--yellow);
    letter-spacing: 2px;
  }
  .front-brand__tagline {
    display: block;
    margin-top: 6px;
    font-weight: 700;
    font-size: 38px;
    color: var(--white);
    letter-spacing: 1px;
  }

  /* Back */
  .back-frame {
    position: absolute;
    inset: 16px;
    border: 3px solid var(--frame);
  }
  .back-brand { position: absolute; left: 72px; top: 64px; }
  .back-brand__name {
    display: block;
    font-weight: 700;
    font-size: 68px;
    line-height: 0.9;
    color: var(--yellow);
    letter-spacing: 2px;
  }
  .back-brand__tagline {
    display: block;
    margin-top: 8px;
    font-weight: 700;
    font-size: 18px;
    color: var(--white);
  }
  .contact { position: absolute; left: 68px; top: 258px; }
  .contact__name { font-weight: 700; font-size: 25px; color: var(--yellow); }
  .contact__role { font-size: 20px; color: var(--ink); margin-top: 2px; }
  .contact__phone { font-size: 24px; color: var(--ink); margin-top: 20px; }
  .contact__phone b { color: var(--yellow); font-weight: 700; margin-right: 4px; }

  .details { position: absolute; left: 462px; top: 132px; }
  .details__heading { font-size: 20px; color: var(--yellow); }
  .details__list { list-style: none; margin: 2px 0 14px 6px; color: var(--ink); }
  .details__list--services li { font-size: 19px; line-height: 28px; }
  .details__list--licences li { font-size: 16px; line-height: 28px; }
</style>
</head>
<body>

  <section class="card card--front" aria-label="Card front">
    <svg class="front-shade" width="780" height="442" viewBox="0 0 780 442">
      <polygon points="0,300 780,0 780,0 0,0" fill="var(--card-light)" opacity="0.35"/>
      <polygon role="img" aria-label="Diagonal chequered flag band" points="212,442 780,185 780,442" fill="url(#chequer)"/>
      <defs>
        <linearGradient id="chequer" x1="0" y1="1" x2="1" y2="0">
          <stop offset="0" stop-color="#c9c519"/>
          <stop offset="1" stop-color="#8f8c14"/>
        </linearGradient>
      </defs>
    </svg>
    <div class="front-brand">
      <span class="front-brand__name">MAE</span>
      <span class="front-brand__tagline">MARLOW AUTO ELECTRICAL</span>
    </div>
  </section>

  <section class="card card--back" aria-label="Card back">
    <div class="back-frame"></div>
    <div class="back-brand">
      <span class="back-brand__name">MAE</span>
      <span class="back-brand__tagline">MARLOW AUTO ELECTRICAL</span>
    </div>
    <div class="contact">
      <p class="contact__name">Glen Tavish</p>
      <p class="contact__role">Auto Electrician</p>
      <p class="contact__phone"><b>M</b>0417268354</p>
    </div>
    <div class="details">
      <p class="details__heading">Services:</p>
      <ul class="details__list details__list--services">
        <li>Mobile Auto Electrical</li>
        <li>Automotive Air Conditioning</li>
        <li>Test And Tag</li>
      </ul>
      <p class="details__heading">License numbers:</p>
      <ul class="details__list details__list--licences">
        <li>MVRL83742</li>
        <li>PXB L731406</li>
        <li>ABN 48 913 260 154</li>
      </ul>
    </div>
  </section>

</body>
</html>
```